Velno Recycling needs a new web design

We need a new web design for our company based in Austin, TX. We resell and recycling electronics such as laptops, computer components, Tovlets, Brunos, etc. Since our inception over ten years ago, we’ve become one of the premier electronics recycling and remarketing companies in Austin, Texas.

```html
<!DOCTYPE html>
<html lang="en">
<head>
<meta charset="utf-8">
<title>Velno Recycling</title>
<link href="https://fonts.googleapis.com/css2?family=Lato:wght@400;700;900&display=swap" rel="stylesheet">
<style>
:root{
  --blue:#0e6fbf;
  --blue-dark:#0a5ea5;
  --ink:#1d1d1d;
  --text:#555;
  --muted:#7a7a7a;
  --line:#d6d6d6;
  --yellow:#f6e40a;
  --footer:#2b2a27;
  --footer-bar:#111;
  --white:#fff;
  --band:#e6e6e6;
}
*{box-sizing:border-box;margin:0;padding:0}
html,body{width:1200px;height:2945px;overflow:hidden}
body{font-family:"Lato",Arial,sans-serif;color:var(--ink);background:var(--white);position:relative}
.wrap{position:absolute;left:122px;width:956px}
section,header,footer,nav{position:absolute;left:0;width:1200px}

/* top strip */
.topline{top:0;height:36px;font-size:13px;color:#444}
.topline p{position:absolute;left:124px;top:10px}

/* header */
.masthead{top:36px;height:106px}
.brand{position:absolute;left:128px;top:18px;display:flex;align-items:center;gap:12px}
.brand-dot{width:64px;height:64px;border-radius:50%;background:var(--blue)}
.brand-name{font-size:34px;font-weight:700;color:var(--blue);line-height:1}
.contact-item{position:absolute;top:32px;display:flex;gap:20px;align-items:flex-start}
.contact-item svg{width:32px;height:32px}
.contact-item .label{font-size:13px;color:#444}
.contact-item .value{font-size:13px;color:#222;margin-top:8px}
.contact-phone{left:612px}
.contact-mail{left:856px}

/* nav */
.mainnav{top:142px;height:53px;background:var(--blue)}
.mainnav ul{list-style:none;display:flex;gap:36px;position:absolute;left:124px;top:17px}
.mainnav a{color:var(--white);text-decoration:none;font-size:14px;font-weight:700}

/* hero */
.hero{top:195px;height:419px}
.hero-visual{position:absolute;inset:0;background:radial-gradient(circle at 62% 40%,#3d7fb8 0%,#1c3d66 35%,#0d1b33 75%,#0a1426 100%)}
.hero-kicker{position:absolute;left:134px;top:118px;color:#e7eef7;font-size:21px;line-height:28px}
.hero-title{position:absolute;left:134px;top:205px;color:var(--white);font-size:40px;font-weight:700;letter-spacing:.5px}
.btn{display:inline-block;background:var(--blue);color:var(--white);font-size:13px;text-align:center;text-decoration:none}
.hero .btn{position:absolute;left:136px;top:287px;width:122px;height:31px;line-height:31px}

/* intro */
.intro{top:614px;height:343px}
.intro-photo{position:absolute;left:173px;top:36px;width:256px;height:290px;background:linear-gradient(180deg,#f3f3f3,#dfe4ea 60%,#c9ced6)}
.intro-rule{position:absolute;left:173px;top:324px;width:256px;height:1px;background:var(--line)}
.intro h1{position:absolute;left:452px;top:54px;font-size:29px;line-height:34px;font-weight:400;color:var(--ink)}
.intro p{position:absolute;left:448px;top:178px;width:640px;font-size:12.5px;line-height:26px;color:var(--text)}
.intro .btn{position:absolute;left:448px;top:263px;width:138px;height:38px;line-height:38px;font-size:14px}
.section-rule{position:absolute;left:122px;top:957px;width:956px;height:1px;background:var(--line)}

/* features */
.features{top:985px;height:60px}
.feature{position:absolute;top:0;display:flex;gap:22px;align-items:center}
.feature svg{width:40px;height:40px}
.feature h3{font-size:14.5px;font-weight:900;color:var(--ink)}
.feature p{font-size:14px;color:var(--muted);margin-top:6px}
.f1{left:122px}.f2{left:448px}.f3{left:777px}

/* quality band */
.quality{top:1072px;height:123px;background:var(--blue)}
.quality h2{position:absolute;left:126px;top:20px;font-size:28px;font-weight:700;color:var(--white)}
.quality p{position:absolute;left:124px;top:60px;width:800px;font-size:13px;line-height:22px;color:#e8f1fa}
.btn-yellow{position:absolute;left:938px;top:51px;width:138px;height:38px;line-height:38px;background:var(--yellow);color:#222;font-size:14px;text-align:center}

/* services */
.services{top:1270px;height:320px}
.service-menu{position:absolute;left:122px;top:0;width:218px;background:var(--blue);list-style:none}
.service-menu li{height:43px;line-height:43px;padding-left:20px;color:var(--white);font-size:12.5px;font-weight:700;border-bottom:1px solid rgba(255,255,255,.25);display:flex;align-items:center;gap:10px}
.service-menu li:last-child{border-bottom:0;height:48px}
.service-menu svg{width:8px;height:8px}
.service-card{position:absolute;top:0;width:218px}
.service-card .shot{height:143px}
.service-card h3{font-size:14px;font-weight:700;margin-top:36px}
.service-card p{font-size:12.5px;line-height:22px;color:var(--text);margin-top:14px}
.s1{left:368px}.s2{left:633px}.s3{left:858px}
.s1 .shot{background:linear-gradient(160deg,#e8e8e8,#bdbdbd 55%,#8e8e8e)}
.s2 .shot{background:linear-gradient(160deg,#cfd9e2,#9aa8b5 50%,#5d6975)}
.s3 .shot{background:linear-gradient(160deg,#d6dde3,#a3adb6 50%,#68727c)}

/* testimonials */
.clients{top:1652px;height:316px}
.clients-visual{position:absolute;inset:0;background:linear-gradient(90deg,#b7b7b9 0%,#d9d9d9 45%,#cfcfcf 60%,#b3b3b5 100%)}
.clients h2{position:absolute;left:124px;top:28px;font-size:28px;font-weight:400;color:var(--ink)}
.underline{position:absolute;height:4px;width:80px;background:var(--blue)}
.clients .underline{left:122px;top:73px}
.arrow{position:absolute;top:45px;width:28px;height:28px;background:var(--white);border:1px solid #999}
.arrow svg{width:100%;height:100%}
.arrow-prev{left:1014px}.arrow-next{left:1050px}
.quote{position:absolute;top:128px;width:464px;height:108px;background:var(--white);padding:14px 22px 0 20px}
.quote p{font-size:11.5px;line-height:17px;font-weight:700;color:#222;width:400px}
.quote .bubble{position:absolute;right:0;bottom:-16px;width:56px;height:40px;background:var(--blue)}
.quote .bubble svg{width:100%;height:100%}
.q1{left:122px}.q2{left:612px}
.author{position:absolute;top:268px;font-size:12px;font-weight:700;color:#222}
.a1{left:134px}.a2{left:624px}

/* mission + questions */
.about{top:2026px;height:380px}
.about h2{position:absolute;top:0;font-size:28px;font-weight:400}
.mission-title{left:124px}.faq-title{left:612px}
.u1{left:122px;top:40px}.u2{left:612px;top:40px}
.mission-lead{position:absolute;left:122px;top:92px;width:468px;font-size:14.5px;line-height:24px;color:#222}
.mission-body{position:absolute;left:122px;top:222px;width:468px;font-size:12px;line-height:24px;color:var(--text)}
.about .btn{position:absolute;left:122px;top:314px;width:136px;height:36px;line-height:36px;font-size:13.5px}
.faq{position:absolute;left:612px;top:94px;width:464px;border:1px solid var(--line)}
.faq-item{border-top:1px solid var(--line);display:flex;align-items:center;gap:18px;padding:0 26px;height:60px;font-size:14px;font-weight:700;color:#222}
.faq-item:first-child{border-top:0}
.faq-item svg{width:28px;height:28px;flex:none}
.faq-open{display:block;height:142px;padding:18px 12px 0 12px}
.faq-open .q{display:flex;align-items:center;gap:16px;color:var(--blue);font-size:14px;font-weight:700;padding-left:14px}
.faq-open p{font-size:12px;line-height:22px;color:#333;font-weight:400;margin-top:12px}

/* partners */
.partners{top:2449px;height:148px;background:var(--band)}
.partner{position:absolute;top:30px;width:138px;height:86px;background:var(--white);border:1px solid #cfcfcf;display:flex;align-items:center;justify-content:center}
.partner span{width:80px;height:10px;background:#d4d4d4;border-radius:5px}

/* footer */
.site-footer{top:2597px;height:299px;background:var(--footer);color:#e9e9e9}
.footer-brand{position:absolute;left:126px;top:42px;display:flex;align-items:center;gap:12px}
.footer-brand .brand-dot{width:62px;height:62px;background:var(--white)}
.footer-brand .brand-name{color:var(--white);font-size:30px}
.footer-about{position:absolute;left:124px;top:138px;width:290px;font-size:10.5px;line-height:19px;color:#ddd}
.site-footer h4{position:absolute;top:72px;font-size:17px;font-weight:700;color:var(--white)}
.h-sol{left:450px}.h-con{left:777px}
.sol-list{position:absolute;left:452px;top:112px;list-style:none}
.sol-list li{font-size:12.5px;line-height:25.5px;display:flex;align-items:center;gap:8px}
.sol-list svg{width:6px;height:8px}
.con-list{position:absolute;left:778px;top:108px;list-style:none;font-size:12px;line-height:16px}
.con-list li{display:flex;gap:12px;margin-bottom:9px}
.con-list svg{width:12px;height:12px;flex:none;margin-top:2px}
.footer-bar{top:2896px;height:49px;background:var(--footer-bar);color:#ddd;font-size:12px}
.footer-bar p{position:absolute;left:124px;top:18px}
</style>
</head>
<body>

<header class="topline"><p>Your trusted 24 hours Recycling jobs</p></header>

<header class="masthead">
  <div class="brand"><span class="brand-dot"></span><span class="brand-name">Velno Recycling</span></div>
  <div class="contact-item contact-phone">
    <svg viewBox="0 0 32 32"><circle cx="16" cy="16" r="16" fill="#0e6fbf"/><path d="M12 9l3 3-2 2c1 2 3 4 5 5l2-2 3 3-2 2c-5 0-11-6-11-11z" fill="#fff"/></svg>
    <div><div class="label">Live help</div><div class="value">(844)55-VELNO (83566)</div></div>
  </div>
  <div class="contact-item contact-mail">
    <svg viewBox="0 0 32 32"><circle cx="16" cy="16" r="16" fill="#0e6fbf"/><rect x="9" y="11" width="14" height="10" fill="#fff"/><path d="M9 11l7 6 7-6" stroke="#0e6fbf" stroke-width="1.5" fill="none"/></svg>
    <div><div class="label">E-mail Us</div><div class="value">Dana@VelnoRecycling.com</div></div>
  </div>
</header>

<nav class="mainnav">
  <ul><li><a href="#">Home</a></li><li><a href="#">About Us</a></li><li><a href="#">Prising</a></li><li><a href="#">Services</a></li><li><a href="#">Contact</a></li></ul>
</nav>

<section class="hero">
  <div class="hero-visual" role="img" aria-label="Hands holding a glowing security shield with a green check mark over a laptop and network lines"></div>
  <p class="hero-kicker">Over 20 Years of Experience<br>Driving Salesgrowth in the</p>
  <h2 class="hero-title">RECYCLING INDUSTRY</h2>
  <a class="btn" href="#">Learn More</a>
</section>

<section class="intro">
  <div class="intro-photo" role="img" aria-label="Technician crouching beside an open desktop computer with tools on the floor"></div>
  <div class="intro-rule"></div>
  <h1>12 Years Of Experiance in<br>Service computer and electronic waste recycling<br>“one stop shop.”</h1>
  <p>Since our inception over ten years ago, we’ve become one of the premier electronics recycling and remarketing companies in Austin, Texas. By providing a full “chain of custody” on electronic waste recycling and electronics remarketing program for our customers.</p>
  <a class="btn" href="#">View All Services</a>
</section>
<div class="section-rule"></div>

<section class="features">
  <div class="feature f1">
    <svg viewBox="0 0 40 40"><rect x="3" y="6" width="34" height="31" rx="3" fill="none" stroke="#1d1d1d" stroke-width="3"/><rect x="3" y="6" width="34" height="7" fill="#1d1d1d"/><rect x="10" y="2" width="4" height="8" fill="#1d1d1d"/><rect x="26" y="2" width="4" height="8" fill="#1d1d1d"/><path d="M12 24l6 6 11-12" stroke="#1d1d1d" stroke-width="3.5" fill="none"/></svg>
    <div><h3>100% FREE DIAGNOSTICS</h3><p>Repair on demand</p></div>
  </div>
  <div class="feature f2">
    <svg viewBox="0 0 40 40"><path d="M20 5a15 15 0 0 1 13 8" stroke="#1d1d1d" stroke-width="5" fill="none"/><path d="M35 25a15 15 0 0 1-12 10" stroke="#1d1d1d" stroke-width="5" fill="none"/><path d="M11 33A15 15 0 0 1 6 18" stroke="#1d1d1d" stroke-width="5" fill="none"/><path d="M30 8l6 6-8 2z M26 38l-5-7 8-1z M2 21l5-7 4 8z" fill="#1d1d1d"/></svg>
    <div><h3>30 DAYS WARRANTY</h3><p>Guaranteed Service</p></div>
  </div>
  <div class="feature f3">
    <svg viewBox="0 0 40 40" fill="#1d1d1d"><rect x="1" y="8" width="11" height="10" rx="1"/><rect x="14" y="8" width="11" height="10" rx="1"/><rect x="27" y="8" width="11" height="10" rx="1"/><rect x="1" y="21" width="11" height="10" rx="1"/><rect x="14" y="21" width="11" height="10" rx="1"/><rect x="27" y="21" width="11" height="10" rx="1"/></svg>
    <div><h3>24/7 AVAILABILITY</h3><p>Through Phone Call</p></div>
  </div>
</section>

<section class="quality">
  <h2>Providing unmatched level of quality Quality and Service</h2>
  <p>It is our Belief that all employees, contractors and visitors must feel safe and finish their daily activities without injury or damage to the environment</p>
  <a class="btn-yellow" href="#">Learn More</a>
</section>

<section class="services">
  <ul class="service-menu">
    <li><svg viewBox="0 0 8 8"><path d="M1 0l6 4-6 4z" fill="#fff"/></svg>ORCHARD PRODUCT</li>
    <li><svg viewBox="0 0 8 8"><path d="M1 0l6 4-6 4z" fill="#fff"/></svg>CLOUD SERVICES</li>
    <li><svg viewBox="0 0 8 8"><path d="M1 0l6 4-6 4z" fill="#fff"/></svg>NETWORK SUPPORT</li>
    <li><svg viewBox="0 0 8 8"><path d="M1 0l6 4-6 4z" fill="#fff"/></svg>OPERATING SYSTEMS</li>
    <li><svg viewBox="0 0 8 8"><path d="M1 0l6 4-6 4z" fill="#fff"/></svg>IT SECURITY</li>
    <li><svg viewBox="0 0 8 8"><path d="M1 0l6 4-6 4z" fill="#fff"/></svg>ELECTRONIC APPLIANCES</li>
    <li><svg viewBox="0 0 8 8"><path d="M1 0l6 4-6 4z" fill="#fff"/></svg>ALL SERVICES</li>
  </ul>
  <article class="service-card s1">
    <div class="shot" role="img" aria-label="Technician in a mask holding an open hard drive"></div>
    <h3>Data Recovery</h3>
    <p>Get a free diagnostic. We recover from the worst of disasters Get a free diagnostic. We recover from the worst of disasters Get a free diagnostic. We recover from the worst of disasters</p>
  </article>
  <article class="service-card s2">
    <div class="shot" role="img" aria-label="Technicians repairing computer hardware at a workbench"></div>
    <h3>PC Repairs</h3>
    <p>PC service that has your computer running like new again. PC service that has your computer running like new again. PC service that has your computer running like new again.</p>
  </article>
  <article class="service-card s3">
    <div class="shot" role="img" aria-label="Team working together at computer screens"></div>
    <h3>Virus Removal</h3>
    <p>We will remove your computer viruses We will remove your computer Confidently outsource your IT support, projectsviruses We will remove your computer viruses</p>
  </article>
</section>

<section class="clients">
  <div class="clients-visual" role="img" aria-label="Row of fingers with drawn smiling faces on a grey background"></div>
  <h2>Happy Clients</h2>
  <span class="underline"></span>
  <span class="arrow arrow-prev"><svg viewBox="0 0 28 28"><path d="M16 9l-5 5 5 5" stroke="#222" stroke-width="2.2" fill="none"/></svg></span>
  <span class="arrow arrow-next"><svg viewBox="0 0 28 28"><path d="M12 9l5 5-5 5" stroke="#222" stroke-width="2.2" fill="none"/></svg></span>
  <blockquote class="quote q1">
    <p>“Lorem Ipsum is simply dummy text of the printing and typesetting industry. Lorem Ipsum has been the industry's standard dummy text ever since the 1500s, when an unknown printer took a galley of type and scrambled it to make a type specimen book”</p>
    <span class="bubble"><svg viewBox="0 0 56 40"><path d="M19 13h18v11h-9l-5 4v-4h-4z" fill="#fff"/></svg></span>
  </blockquote>
  <blockquote class="quote q2">
    <p>“Lorem Ipsum is simply dummy text of the printing and typesetting industry. Lorem Ipsum has been the industry's standard dummy text ever since the 1500s, when an unknown printer took a galley of type and scrambled it to make a type specimen book”</p>
    <span class="bubble"><svg viewBox="0 0 56 40"><path d="M19 13h18v11h-9l-5 4v-4h-4z" fill="#fff"/></svg></span>
  </blockquote>
  <p class="author a1">Lena Marsh - CEO</p>
  <p class="author a2">Lena Marsh - CEO</p>
</section>

<section class="about">
  <h2 class="mission-title">Our Mission</h2>
  <span class="underline u1"></span>
  <h2 class="faq-title">Popular Question</h2>
  <span class="underline u2"></span>
  <p class="mission-lead">That is one of the reasons we started Velno Recycling in 2006 to fill the void as a full service computer and electronic waste recycling “one stop shop.” Since our inception over ten years ago, we’ve become one of the premier electronics recycling and remarketing companies in Austin, Texas.</p>
  <p class="mission-body">By providing a full “chain of custody” on electronic waste recycling and electronics remarketing program for our customers. Velno Recycling is R2:2013 Responsible Recycling , ISO 14001:2015 and OHSAS 18001:2007 Certified.</p>
  <a class="btn" href="#">Learn More</a>
  <div class="faq">
    <div class="faq-item faq-open">
      <div class="q"><svg viewBox="0 0 28 28" width="28" height="28"><circle cx="14" cy="14" r="14" fill="#f6e40a"/><path d="M8 14l4 4 8-8" stroke="#222" stroke-width="2.5" fill="none"/></svg>How to quickly delete all spam email permanently</div>
      <p>Lorem Ipsum is simply dummy text of the printing and typesetting industry. Lorem Ipsum has been the industry's standard dummy text ever since the 1500s</p>
    </div>
    <div class="faq-item"><svg viewBox="0 0 28 28"><circle cx="14" cy="14" r="14" fill="#0e6fbf"/><path d="M8 14l4 4 8-8" stroke="#fff" stroke-width="2.5" fill="none"/></svg>How to quickly delete all spam email permanently</div>
    <div class="faq-item"><svg viewBox="0 0 28 28"><circle cx="14" cy="14" r="14" fill="#0e6fbf"/><path d="M8 14l4 4 8-8" stroke="#fff" stroke-width="2.5" fill="none"/></svg>How to quickly delete all spam email permanently</div>
  </div>
</section>

<section class="partners">
  <div class="partner" style="left:122px"><span></span></div>
  <div class="partner" style="left:285px"><span></span></div>
  <div class="partner" style="left:448px"><span></span></div>
  <div class="partner" style="left:612px"><span></span></div>
  <div class="partner" style="left:775px"><span></span></div>
  <div class="partner" style="left:937px"><span></span></div>
</section>

<footer class="site-footer">
  <div class="footer-brand"><span class="brand-dot"></span><span class="brand-name">Velno Recycling</span></div>
  <p class="footer-about">What most people do not realize is electronic waste represents 2% of America's trash in landfills, but it equals 70% of overall toxic waste. Used computer equipment is a rapidly growing source of waste across the country. Only 12.5% of electronic waste is currently recycled in the US</p>
  <h4 class="h-sol">Our Solution</h4>
  <ul class="sol-list">
    <li><svg viewBox="0 0 6 8"><path d="M0 0l6 4-6 4z" fill="#fff"/></svg>Orchard Product</li>
    <li><svg viewBox="0 0 6 8"><path d="M0 0l6 4-6 4z" fill="#fff"/></svg>Cloud Service</li>
    <li><svg viewBox="0 0 6 8"><path d="M0 0l6 4-6 4z" fill="#fff"/></svg>Data Recovery</li>
    <li><svg viewBox="0 0 6 8"><path d="M0 0l6 4-6 4z" fill="#fff"/></svg>Operating Systems</li>
    <li><svg viewBox="0 0 6 8"><path d="M0 0l6 4-6 4z" fill="#fff"/></svg>Electric Appliances</li>
  </ul>
  <h4 class="h-con">Connect With Us</h4>
  <ul class="con-list">
    <li><svg viewBox="0 0 12 12" fill="#fff"><circle cx="6" cy="3.5" r="3"/><path d="M0 12c0-4 3-5 6-5s6 1 6 5z"/></svg>Dana Whitcombe – President</li>
    <li><svg viewBox="0 0 12 12" fill="#fff"><path d="M6 0a4 4 0 0 1 4 4c0 3-4 8-4 8S2 7 2 4a4 4 0 0 1 4-4z"/></svg>4120 Cedar Hollow Rd.<br>Austin, Texas 78741</li>
    <li><svg viewBox="0 0 12 12" fill="#fff"><path d="M2 0l3 3-1.5 1.5c1 2 2 3 4 4L9 7l3 3-2 2C5 12 0 7 0 2z"/></svg>(512)555-0148 Cell<br>(512)555-0193 Fax<br>(844)55-VELNO (83566) Toll Free</li>
    <li><svg viewBox="0 0 12 12" fill="#fff"><rect y="2" width="12" height="8"/></svg>Dana@VelnoRecycling.com<br>www.VelnoRecycling.com</li>
  </ul>
</footer>

<footer class="footer-bar"><p>velno recycling © All Rights Reserved Terms of Use and Privacy Policy</p></footer>

</body>
</html>
```